43 Year Old Construction firm needs Updated Business Card & Stationery Design

We are an established and well known (in our market) commercial construction firm. We need a cleaner and more modern look for our corporate identity material. We would like to continue to use our current colors and logo.
We are thinking about incorporating a slogan on our business card (either front or back): "Striving to be the most trusted builder in our market." The text could change at some point. Our website is www.kvoplarn.com . Sample card is attached. Some will have more phone numbers, etc...
Updates

Target Market(s)

Commercial and institutional clients.

Industry/Entity Type

Construction Company

Contact Information for Business Card

See attached for existing card. But don't be constrained.

Requirements
Must have
• Logo, name, title, address, website, email, phone numbers (as few as one, as many as three)
• Slogan on front or back "Striving to be the most trusted builder in our market"
• Use existing logo and colors

```html
<!DOCTYPE html>
<html lang="en">
<head>
<meta charset="utf-8">
<title>Kvoplarn Constructors – Business Card</title>
<link rel="stylesheet" href="https://fonts.googleapis.com/css2?family=Lato:wght@400;700&display=swap">
<style>
  :root {
    --navy: #1c4079;
    --green: #00874a;
    --ink: #4f4f4f;
    --paper: #ffffff;
  }
  html, body {
    margin: 0;
    padding: 0;
    width: 1200px;
    height: 702px;
    overflow: hidden;
    background: var(--paper);
  }
  .card {
    position: relative;
    width: 1200px;
    height: 702px;
    background: var(--paper);
    font-family: "Lato", Arial, sans-serif;
    overflow: hidden;
  }
  .brand {
    position: absolute;
    right: 91px;
    top: 118px;
    display: flex;
    align-items: center;
    gap: 16px;
    color: var(--navy);
    font-weight: 700;
    font-size: 40px;
    line-height: 1;
    letter-spacing: 0.5px;
  }
  .brand-square {
    width: 26px;
    height: 26px;
    background: var(--green);
  }
  .brand-rule {
    position: absolute;
    right: 91px;
    top: 184px;
    width: 452px;
    height: 4px;
    background: var(--green);
  }
  .slogan {
    position: absolute;
    right: 91px;
    top: 204px;
    width: 452px;
    margin: 0;
    color: var(--navy);
    font-size: 21px;
    line-height: 28px;
    text-align: right;
  }
  .person {
    position: absolute;
    left: 98px;
    top: 358px;
  }
  .person-name {
    margin: 0;
    color: var(--navy);
    font-weight: 700;
    font-size: 44px;
    line-height: 1.1;
  }
  .person-title {
    margin: 4px 0 0;
    color: var(--ink);
    font-size: 33px;
    line-height: 1.2;
  }
  .contact {
    position: absolute;
    left: 98px;
    top: 488px;
    margin: 0;
    color: var(--ink);
    font-size: 33px;
    line-height: 46px;
    font-style: normal;
  }
  .address {
    position: absolute;
    right: 91px;
    top: 532px;
    margin: 0;
    color: var(--ink);
    font-size: 33px;
    line-height: 46px;
    text-align: right;
    font-style: normal;
  }
  .footer-band {
    position: absolute;
    left: 0;
    bottom: 0;
    width: 1200px;
    height: 64px;
    background: var(--navy);
  }
  .web-tab {
    position: absolute;
    left: 856px;
    bottom: 0;
    width: 248px;
    height: 64px;
    background: var(--green);
    border-left: 7px solid var(--paper);
    border-right: 7px solid var(--paper);
    color: var(--paper);
    font-size: 25px;
    text-align: center;
    line-height: 38px;
    white-space: nowrap;
  }
</style>
</head>
<body>
  <div class="card">
    <div class="brand">
      <span class="brand-square"></span>
      <span class="brand-name">Kvoplarn Constructors</span>
    </div>
    <div class="brand-rule"></div>
    <p class="slogan">Striving to be the most trusted builder in our market.</p>

    <div class="person">
      <h1 class="person-name">Daniel R. Marlowe</h1>
      <p class="person-title">President</p>
    </div>

    <address class="contact">
      314.555.0142<br>
      314.555.0187<br>
      danm@kvoplarn.com
    </address>

    <address class="address">
      4410 Ridgeline Avenue<br>
      St. Louis, Missouri 63119
    </address>

    <div class="footer-band"></div>
    <div class="web-tab">www.kvoplarn.com</div>
  </div>
</body>
</html>
```